Webdesign for development of custom specific electronics
Zielgruppe
We are specialised in development of custom specific electronics.
We also produce and test the pcb assemblies for our customers .
We sell some of our own products as well.
Aufgabenstellung
We provide an detailed briefing in a separate file.

```html
<!DOCTYPE html>
<html lang="de">
<head>
<meta charset="utf-8">
<title>Trusk Halvorsen – Elektronikentwicklung</title>
<link href="https://fonts.googleapis.com/css2?family=Signika:wght@300;400;500&display=swap" rel="stylesheet">
<style>
:root{
  --navy-deep:#0c1f3f;
  --navy:#123466;
  --blue:#2a8fd3;
  --blue-btn:#2b8fd1;
  --gray-bg:#efefef;
  --text-gray:#555;
  --line:#b9b9b9;
  --white:#fff;
}
*{margin:0;padding:0;box-sizing:border-box}
html,body{width:1200px;height:2400px;overflow:hidden}
body{position:relative;font-family:"Signika",sans-serif;background:var(--white);color:var(--text-gray)}
.abs{position:absolute}

.topbar{left:0;top:0;width:1200px;height:51px;background:linear-gradient(90deg,var(--navy-deep),#163663 60%,var(--navy-deep))}
.top-phone{left:601px;top:14px;color:var(--blue);font-size:17px;display:flex;align-items:center;gap:8px;white-space:nowrap}
.top-mail{left:775px;top:16px;color:var(--blue);font-size:13px;display:flex;align-items:center;gap:10px;white-space:nowrap}
.top-social{top:14px;width:22px;height:22px;background:var(--white)}

.navbar{left:0;top:51px;width:1200px;height:81px;background:var(--gray-bg)}
.brand{left:171px;top:73px;display:flex;align-items:center;gap:12px}
.brand-mark{width:34px;height:34px;background:var(--blue)}
.brand-name{font-size:27px;font-weight:400;color:#6b6f75;white-space:nowrap}
.nav{left:540px;top:85px;display:flex;gap:21px;font-size:13px;color:#5a5f66;white-space:nowrap}
.nav-underline{left:530px;top:129px;width:83px;height:3px;background:var(--blue)}

.hero{left:0;top:132px;width:1200px;height:545px;background:radial-gradient(ellipse at 75% 35%,#24599a 0%,#163f77 40%,#0e2a55 85%)}
.hero-img{left:172px;top:199px;width:319px;height:478px;background:linear-gradient(160deg,#2e6fb4,#1b4f95 50%,#143f7c)}
.hero-dip{left:497px;top:676px;width:238px;height:37px;border-radius:0 0 50% 50% / 0 0 100% 100%;background:#133a6f}
.hero-title{left:598px;top:244px;width:480px;font-size:35px;line-height:43px;font-weight:500;color:var(--white)}
.hero-sub{left:601px;top:411px;width:420px;font-size:20px;line-height:28px;font-weight:300;color:var(--white)}
.btn{display:flex;align-items:center;justify-content:center;width:299px;height:44px;border-radius:22px;background:var(--blue-btn);color:var(--white);font-size:17px;font-weight:400}
.hero-btn{left:601px;top:525px}
.down-arrow{left:595px;top:692px}

.welcome-title{left:120px;top:786px;width:307px;text-align:right;font-size:33px;line-height:36px;font-weight:500;color:var(--blue)}
.welcome-text{left:469px;top:788px;width:570px;font-size:14px;line-height:22.4px;font-weight:300;color:var(--text-gray)}

.features{left:0;top:953px;width:1200px;height:886px;background:radial-gradient(ellipse at 50% 55%,#1a4c8a 0%,#123566 45%,#0b2045 90%)}
.feature{top:1037px;width:280px;text-align:center;color:var(--white);font-size:20px;line-height:23px;font-weight:300}
.feature-icon{display:block;margin:0 auto 34px}
.products-title{left:0;top:1280px;width:1200px;text-align:center;font-size:32px;line-height:45px;font-weight:500;color:var(--blue)}
.product-img{left:401px;top:1412px;width:419px;height:252px;border-radius:10px;background:linear-gradient(135deg,#3d7fc2,#2a68ad 55%,#d6d3cf)}
.products-btn{left:461px;top:1716px}

.contact{left:0;top:1839px;width:1200px;height:429px;background:var(--gray-bg)}
.contact-title{left:120px;top:1909px;width:307px;text-align:right;font-size:32px;line-height:36px;font-weight:500;color:var(--blue)}
.field{border-bottom:1px solid var(--line);font-size:17px;font-weight:300;color:#6a6a6a;padding:0 6px 6px}
.f-name{left:471px;top:1916px;width:204px}
.f-mail{left:694px;top:1916px;width:204px}
.f-msg{left:469px;top:1961px;width:429px;height:143px;padding:0 9px}
.contact-btn{left:461px;top:2155px}

.footer{left:0;top:2268px;width:1200px;height:132px;background:linear-gradient(90deg,#0f2a55,#183f77 50%,#0f2a55)}
.footer-col{top:2313px;font-size:13.5px;line-height:23px;font-weight:300;color:#dfe7f2;white-space:nowrap}
</style>
</head>
<body>

<header>
  <div class="abs topbar"></div>
  <div class="abs top-phone">
    <svg width="16" height="16" viewBox="0 0 24 24"><path fill="#2a8fd3" d="M6.6 10.8a15 15 0 0 0 6.6 6.6l2.2-2.2c.3-.3.7-.4 1-.2 1.1.4 2.3.6 3.6.6.6 0 1 .4 1 1V20c0 .6-.4 1-1 1A17 17 0 0 1 3 4c0-.6.4-1 1-1h3.5c.6 0 1 .4 1 1 0 1.3.2 2.5.6 3.6.1.3 0 .7-.2 1z"/></svg>
    08192/4410 583
  </div>
  <div class="abs top-mail">
    <svg width="18" height="13" viewBox="0 0 18 13"><rect width="18" height="13" rx="1" fill="#fff"/><path d="M1 1l8 6 8-6" stroke="#123466" stroke-width="1.5" fill="none"/></svg>
    service@trusk-halvorsen.de
  </div>
  <div class="abs top-social" style="left:993px" aria-label="Profil"></div>
  <div class="abs top-social" style="left:1025px" aria-label="Netzwerk"></div>

  <div class="abs navbar"></div>
  <div class="abs brand"><span class="brand-mark"></span><span class="brand-name">Trusk Halvorsen</span></div>
  <nav class="abs nav">
    <span>ÜBER UNS</span><span>PRODUKTE</span><span>ENTWICKLUNG</span><span>FERTIGUNG</span><span>SERVICE</span><span>KONTAKT</span>
  </nav>
  <div class="abs nav-underline"></div>
</header>

<section>
  <div class="abs hero" role="img" aria-label="Dunkelblauer Hintergrund mit Leiterplattenstrukturen"></div>
  <div class="abs hero-dip"></div>
  <div class="abs hero-img" role="img" aria-label="Foto einer blauen bestückten Leiterplatte"></div>
  <h1 class="abs hero-title">Elektronikentwicklung und Fertigung von Schaltungen &amp; Baugruppen</h1>
  <p class="abs hero-sub">Wir bieten Ihnen eine uneingeschränkte<br>5-jährige Zufriedenheitsgarantie</p>
  <div class="abs btn hero-btn">Kontakt aufnehmen</div>
  <svg class="abs down-arrow" width="30" height="50" viewBox="0 0 30 50"><path d="M15 2v44M3 34l12 12 12-12" stroke="#2a8fd3" stroke-width="3" fill="none" stroke-linecap="round"/></svg>
</section>

<section>
  <h2 class="abs welcome-title">Willkommen<br>in der Welt<br>der Elektronik</h2>
  <p class="abs welcome-text">Lorem ipsum dolor sit amet, consectetur adipiscing elit, sed do eiusmod tempor incididunt ut labore et dolore magna aliqua. Ut enim ad minim veniam, quis nostrud exercitation ullamco laboris nisi ut aliquip ex ea commodo consequat. Duis aute irure dolor in reprehe in voluptate velit esse cillum dolore eu fugiat nulla pariatur. Excepteur sint occaecat cupidatat non proident, sunt in culpa qui officia deserunt mollit anim id est laborum.</p>
</section>

<section>
  <div class="abs features" role="img" aria-label="Dunkelblauer Technik-Hintergrund mit Platinenlinien"></div>
  <div class="abs feature" style="left:171px">
    <svg class="feature-icon" width="62" height="76" viewBox="0 0 62 76"><path d="M18 44L8 72l10-5 5 9 8-26zM44 44l10 28-10-5-5 9-8-26z" fill="#2a8fd3"/><circle cx="31" cy="30" r="28" fill="#2a8fd3"/><circle cx="31" cy="30" r="15" fill="none" stroke="#123566" stroke-width="6"/></svg>
    Direkt bei unseren OEM Partnerunternehmen
  </div>
  <div class="abs feature" style="left:473px">
    <svg class="feature-icon" width="68" height="64" viewBox="0 0 68 64"><rect x="2" y="8" width="64" height="54" fill="#2a8fd3"/><rect x="2" y="16" width="64" height="3" fill="#123566"/><rect x="16" y="0" width="5" height="14" fill="#2a8fd3"/><rect x="47" y="0" width="5" height="14" fill="#2a8fd3"/><text x="34" y="54" text-anchor="middle" font-family="Signika,sans-serif" font-size="32" font-weight="500" fill="#fff">5</text></svg>
    5-Jährige<br>Zufriedenheitsgarantie
  </div>
  <div class="abs feature" style="left:765px">
    <svg class="feature-icon" width="84" height="62" viewBox="0 0 84 62"><rect x="0" y="0" width="84" height="62" fill="#2a8fd3"/><rect x="24" y="14" width="36" height="34" fill="none" stroke="#123566" stroke-width="4"/><rect x="33" y="23" width="18" height="16" fill="#123566"/><path d="M0 10h18M0 31h18M0 52h18M66 10h18M66 31h18M66 52h18M30 0v10M54 0v10M30 52v10M54 52v10" stroke="#123566" stroke-width="3"/></svg>
    Kundenspezifischen<br>Lösungen
  </div>
  <h2 class="abs products-title">Innovative, qualitativ hochwertige<br>und bezahlbare Produkte</h2>
  <div class="abs product-img" role="img" aria-label="Produktfoto eines Sensorgehäuses für Temperatur und Luftfeuchte vor Platinenlinien"></div>
  <div class="abs btn products-btn">mehr erfahren</div>
</section>

<section>
  <div class="abs contact"></div>
  <h2 class="abs contact-title">Kontaktieren<br>Sie uns einfach</h2>
  <div class="abs field f-name">Name</div>
  <div class="abs field f-mail">E-Mail</div>
  <div class="abs field f-msg">Nachricht</div>
  <div class="abs btn contact-btn">absenden</div>
</section>

<footer>
  <div class="abs footer" role="img" aria-label="Dunkelblauer Platinen-Hintergrund"></div>
  <div class="abs footer-col" style="left:171px">Trusk Halvorsen GmbH &amp; Co. KG<br>86999 Lindenau</div>
  <div class="abs footer-col" style="left:472px">Tel : +49 (0) 8192 4410 583<br>E-Mail: kontakt@trusk-halvorsen.de</div>
  <div class="abs footer-col" style="left:769px">Profil |&nbsp; Netzwerk<br>AGB &nbsp;|&nbsp; Datenschutz &nbsp;|&nbsp; Impressum</div>
</footer>

</body>
</html>
```